RTQ Flyer

We need a two sided flyer that matches the color scheme of the logo. Should use left justified formatting. Needs to reflect diversity in terms of race and gender. Should have a clean and uncluttered look and feel. Add the following tag line: Helping Public Sector Organizations Work Smarter

```html
<!DOCTYPE html>
<html lang="en">
<head>
<meta charset="utf-8">
<title>RTQ Flyer</title>
<link href="https://fonts.googleapis.com/css2?family=League+Spartan:wght@700&family=Exo+2:wght@300;400;600;700&display=swap" rel="stylesheet">
<style>
  :root {
    --olive: #7d6d23;
    --olive-light: #b4ab82;
    --ink: #1c1c1c;
    --paper: #ffffff;
    --backdrop: #e9e6df;
    --wash: #f3f3ee;
  }
  * { margin: 0; padding: 0; box-sizing: border-box; }
  html, body { width: 1200px; height: 1200px; overflow: hidden; background: var(--backdrop); }
  .flyer {
    position: absolute; left: 179px; top: 55px;
    width: 1053px; height: 1362px;
    background: var(--paper);
    transform: scale(0.8); transform-origin: 0 0;
    font-family: "Exo 2", sans-serif; color: var(--ink);
    overflow: hidden;
    box-shadow: 0 6px 24px rgba(0,0,0,.18);
  }
  .hero {
    position: absolute; left: 0; top: 0; width: 1053px; height: 338px;
    background: linear-gradient(115deg, #3fa9c9 0%, #2c7f98 35%, #4e5a4c 62%, #5d5a2c 82%, #3b4a35 100%);
  }
  .hero-rule { position: absolute; left: 0; top: 338px; width: 1053px; height: 8px; background: var(--olive); }
  .brand-dot {
    position: absolute; left: 476px; top: 288px; width: 100px; height: 100px;
    border-radius: 50%; background: var(--olive);
  }
  .brand-name {
    position: absolute; left: 0; top: 398px; width: 1053px; text-align: center;
    font-family: "League Spartan", sans-serif; font-weight: 700; font-size: 56px; line-height: 60px;
  }
  .tagline {
    position: absolute; left: 0; top: 467px; width: 1053px; text-align: center;
    font-weight: 300; font-size: 24px; line-height: 30px;
  }
  .section-bar { position: absolute; left: 0; width: 52px; height: 16px; background: var(--olive); }
  .section-title {
    position: absolute; left: 75px; font-weight: 600; font-size: 28px; line-height: 32px; color: var(--olive);
  }
  .block { position: absolute; left: 75px; width: 905px; }
  .body { font-size: 22.5px; line-height: 27.5px; }
  .body.justified { text-align: justify; text-align-last: left; }
  .sub { font-weight: 700; font-size: 22.5px; line-height: 28px; }
  .small { font-size: 20.5px; line-height: 26px; }
  .bullets { list-style: none; }
  .bullets li { position: relative; padding-left: 34px; font-size: 21px; }
  .bullets li::before {
    content: ""; position: absolute; left: 0; top: 6px; width: 17px; height: 17px;
    border-radius: 50%; background: var(--olive);
  }
  .about-list li { line-height: 23px; margin-bottom: 5px; width: 810px; }
  .deliverables li { line-height: 27.5px; }
  .corner { position: absolute; left: 0; top: 0; }
</style>
</head>
<body>
  <main class="flyer">
    <svg class="corner" width="1053" height="1362" viewBox="0 0 1053 1362" role="img" aria-label="Decorative olive fan shape in the lower right corner">
      <defs>
        <linearGradient id="corner-tone" x1="0" y1="0" x2="1" y2="0">
          <stop offset="0" stop-color="#b4ab82"/>
          <stop offset="1" stop-color="#7d6d23"/>
        </linearGradient>
      </defs>
      <polygon points="0,1362 881,1167 1053,1150 1053,1362" fill="var(--wash)"/>
      <polygon points="734,1362 881,1167 1053,1150 1053,1362" fill="url(#corner-tone)"/>
    </svg>

    <div class="hero" role="img" aria-label="Photo of a diverse team of four colleagues leaning over a table working together, tinted teal and olive"></div>
    <div class="hero-rule"></div>
    <div class="brand-dot"></div>

    <h1 class="brand-name">Rowan Tate Quorum</h1>
    <p class="tagline">Helping Public Sector Organizations Work Smarter</p>

    <div class="section-bar" style="top:518px"></div>
    <h2 class="section-title" style="top:511px">About Rowan Tate Quorum (RTQ)</h2>
    <p class="block body" style="top:543px">RTQ is a public sector focused management consulting firm providing facilitation and advisory support services in the areas of:</p>
    <ul class="block bullets about-list" style="top:607px">
      <li>Strategic planning, utilizing the proprietary Focus Page Plan® Model (also known as the FPP®)</li>
      <li>Performance Management and Data Analytics (tracking and measuring what matters, while also driving desired results)</li>
    </ul>
    <p class="block body justified" style="top:714px;width:903px">RTQ is able to bring to any engagement experienced consultants with decades of knowledge and experience garnered from working at all levels of government as chief financial officer, chief procurement officer, chief operating officer and as city manager.</p>

    <div class="section-bar" style="top:818px"></div>
    <h2 class="section-title" style="top:811px">Our Services</h2>
    <h3 class="block sub" style="top:848px">The Focus Page Plan® (aka FPP®)</h3>
    <p class="block small" style="top:887px;width:895px">&nbsp;"A Suite of Focus Page Solutions®” custom fit to the organization and the business situation at hand.&nbsp; The work group is the top management team for the organization, who are responsible for overall strategic direction of the organization. "The process involves an initial strategic assessment, 2-3 work sessions with strategic mapping homework in between each session, over an 8-10 week time span.”.</p>

    <div class="section-bar" style="top:1042px"></div>
    <h2 class="section-title" style="top:1034px">FPP® Deliverables</h2>
    <ul class="block bullets deliverables" style="top:1066px">
      <li>An actionable strategic plan on one page - FPP®: Objective, Goals, Strategies, Plans.</li>
      <li>Critical path detail for each FPP® page Plan.</li>
      <li>FPP Scorecard® to teach progress of all desired outcomes.</li>
      <li>Not-Now List® to clearly outline work to Stop, Hold or Limit.</li>
      <li>Resources &amp; Barriers analysis to align capability with commitments.</li>
      <li>Assessment of "relative priority" across all key projects.</li>
      <li>Deployment plan – initial and on-going.</li>
      <li>Periodic Review and annual renewal of the strategic plan.</li>
      <li>Training of an Internal FPP® Process owner</li>
    </ul>
  </main>
</body>
</html>
```